Baby Shower Invitation for Vectored Image Provided

Caroline & Desmond's Baby Shower - Black/White/Gold Colors preferred
Please use the vectored portrait image attached. I'd like us on the lower right side of the invitation.
Can be horizontal or vertical layout.
The second image attached has the information needed for you to complete.
I don't want that style copied, it is just an example.

```html
<!DOCTYPE html>
<html lang="en">
<head>
<meta charset="utf-8">
<title>Baby Shower Invitation – Caroline Whitmore</title>
<link rel="stylesheet" href="https://fonts.googleapis.com/css2?family=Arimo:wght@400;700&family=Great+Vibes&family=Yesteryear&family=Tinos:ital,wght@1,700&family=Parisienne&display=swap">
<style>
  :root {
    --gold: #c9a227;
    --gold-deep: #a88418;
    --gold-light: #ecd58a;
    --cream: #ffffff;
    --ink: #111111;
    --charcoal: #1f1f1f;
  }
  * { margin: 0; padding: 0; box-sizing: border-box; }
  html, body { width: 848px; height: 1200px; overflow: hidden; background: var(--cream); }
  .invitation {
    position: relative;
    width: 848px;
    height: 1200px;
    overflow: hidden;
    background:
      radial-gradient(ellipse 560px 660px at 45% 50%, var(--cream) 0%, rgba(255,255,255,0.9) 40%, rgba(255,255,255,0) 80%),
      linear-gradient(160deg, var(--gold-deep) 0%, var(--gold) 28%, var(--gold-light) 55%, var(--gold) 82%, var(--gold-deep) 100%);
    color: var(--ink);
    font-family: "Arimo", Arial, sans-serif;
  }
  .frame-line {
    position: absolute; inset: 16px;
    border: 2px solid var(--ink);
    pointer-events: none;
  }
  .headline-art { position: absolute; left: 0; top: 0; width: 848px; height: 330px; }
  .exclaim {
    position: absolute; top: 36px; left: 0; width: 100%;
    text-align: center; font-family: "Great Vibes", cursive; font-weight: 400;
    font-size: 60px; word-spacing: 14px; color: var(--ink);
  }
  .invite-line {
    position: absolute; top: 368px; left: 0; width: 100%;
    text-align: center; font-family: "Parisienne", cursive; font-size: 35px;
  }
  .honoree {
    position: absolute; top: 425px; left: 0; width: 100%;
    text-align: center; font-family: "Yesteryear", cursive; font-weight: 400; font-size: 58px;
  }
  .details-panel {
    position: absolute; left: 0; top: 523px; width: 490px; height: 354px;
    background: rgba(255,255,255,0.45);
    border-right: 3px solid var(--ink);
  }
  .footprints-art {
    position: absolute; left: 600px; top: 540px; width: 144px; height: 182px;
    border-radius: 50%;
    background: radial-gradient(ellipse, rgba(17,17,17,0.18), rgba(17,17,17,0));
  }
  .detail { position: absolute; left: 36px; display: flex; align-items: flex-start; }
  .detail svg { flex: none; }
  .detail-text { line-height: 1.6; }
  .detail-date { top: 562px; }
  .detail-date .detail-text { font-size: 24px; font-weight: 700; margin-left: 16px; margin-top: -4px; line-height: 1.62; }
  .detail-date sup { font-size: 15px; vertical-align: 10px; margin-right: 4px; }
  .detail-place { top: 668px; }
  .detail-place .detail-text { font-size: 23px; font-weight: 700; margin-left: 21px; margin-top: -6px; line-height: 1.8; }
  .detail-rsvp { top: 783px; }
  .detail-rsvp .detail-text { font-size: 21px; font-weight: 700; margin-left: 22px; margin-top: -5px; line-height: 1.6; }
  .portrait-art {
    position: absolute; left: 503px; top: 738px; width: 345px; height: 462px;
    background: linear-gradient(180deg, rgba(31,31,31,0) 0%, rgba(31,31,31,0.55) 18%, #262626 45%, var(--charcoal) 100%);
    border-radius: 160px 140px 0 0;
  }
  .pram-art {
    position: absolute; left: 28px; top: 900px; width: 440px; height: 250px;
    border-radius: 220px 220px 40px 40px;
    background: linear-gradient(90deg, #fbf3d6, var(--gold-light) 50%, #fbf3d6);
    opacity: 0.8;
  }
  .registry {
    position: absolute; left: 112px; top: 960px;
    font-family: "Tinos", "Times New Roman", serif; font-style: italic; font-weight: 700;
    font-size: 21.5px; line-height: 2;
  }
</style>
</head>
<body>
<main class="invitation">
  <div class="frame-line"></div>

  <svg class="headline-art" viewBox="0 0 848 330">
    <defs>
      <linearGradient id="bunting-tone" x1="0" x2="1">
        <stop offset="0" stop-color="#111111"/>
        <stop offset="0.25" stop-color="#f5f0e0"/>
        <stop offset="0.5" stop-color="#c9a227"/>
        <stop offset="0.75" stop-color="#f5f0e0"/>
        <stop offset="1" stop-color="#111111"/>
      </linearGradient>
      <path id="arc-line" d="M 62 165 Q 425 432 792 150"/>
    </defs>
    <path role="img" aria-label="Garland of pennant flags in black, white and gold"
          d="M 22 0 L 826 0 Q 820 20 800 70 Q 440 330 50 60 Q 30 30 22 0 Z"
          fill="url(#bunting-tone)" opacity="0.55"/>
    <text font-family="Arimo, Arial, sans-serif" font-weight="700" font-size="38" fill="#111" letter-spacing="1">
      <textPath href="#arc-line" startOffset="50%" text-anchor="middle">A LITTLE MAN IS ON THE WAY !</textPath>
    </text>
  </svg>

  <h1 class="exclaim">Oh Boy !</h1>
  <p class="invite-line">Please join us for a Baby Shower honoring</p>
  <h2 class="honoree">Caroline Whitmore</h2>

  <div class="details-panel"></div>
  <div class="footprints-art" role="img" aria-label="Outline of two baby footprints"></div>

  <div class="detail detail-date">
    <svg width="64" height="66" viewBox="0 0 64 66" aria-hidden="true">
      <rect x="3" y="8" width="48" height="44" rx="4" fill="none" stroke="#111" stroke-width="3"/>
      <rect x="3" y="8" width="48" height="10" fill="#111"/>
      <rect x="12" y="2" width="4" height="11" rx="2" fill="#111"/>
      <rect x="38" y="2" width="4" height="11" rx="2" fill="#111"/>
      <g fill="#111">
        <rect x="9" y="23" width="6" height="5"/><rect x="18" y="23" width="6" height="5"/><rect x="27" y="23" width="6" height="5"/><rect x="36" y="23" width="6" height="5"/>
        <rect x="9" y="31" width="6" height="5"/><rect x="18" y="31" width="6" height="5"/><rect x="27" y="31" width="6" height="5"/>
        <rect x="9" y="39" width="6" height="5"/><rect x="18" y="39" width="6" height="5"/>
      </g>
      <circle cx="47" cy="50" r="13" fill="#fff" stroke="#111" stroke-width="3"/>
      <path d="M47 42 V50 H54" fill="none" stroke="#111" stroke-width="2.5"/>
    </svg>
    <p class="detail-text">1<sup>st</sup>September,Saturday<br>between 11:30am - 2.30pm</p>
  </div>

  <div class="detail detail-place">
    <svg width="60" height="70" viewBox="0 0 60 70" aria-hidden="true">
      <path d="M30 2 C17 2 9 12 9 23 C9 37 30 55 30 55 C30 55 51 37 51 23 C51 12 43 2 30 2 Z" fill="#111"/>
      <circle cx="30" cy="22" r="7" fill="#fff"/>
      <ellipse cx="30" cy="60" rx="26" ry="7" fill="none" stroke="#111" stroke-width="3.5"/>
    </svg>
    <p class="detail-text">The Ashford Room<br>1482 Crestline Ave. Raleigh, NC</p>
  </div>

  <div class="detail detail-rsvp">
    <svg width="58" height="62" viewBox="0 0 58 62" aria-hidden="true">
      <path d="M4 4 H54 V44 H22 L10 58 V44 H4 Z" fill="none" stroke="#111" stroke-width="3.5" stroke-linejoin="round"/>
      <path d="M18 24 L26 32 L41 16" fill="none" stroke="#111" stroke-width="4.5" stroke-linecap="round" stroke-linejoin="round"/>
    </svg>
    <p class="detail-text">RSVP to Desmond at 919-555-0148<br>by August 20th</p>
  </div>

  <div class="pram-art" role="img" aria-label="Striped black and gold baby pram illustration"></div>
  <p class="registry">Caroline is registered at<br>Little Nest !</p>
  <div class="portrait-art" role="img" aria-label="Illustrated portrait of the expecting couple, dressed in black"></div>
</main>
</body>
</html>
```